Elegant and modern Wedding Photography brochure

My existing brochure (attached) needs a major facelift. This is one of the main selling tools - it gets emailed to my clients when they make an equiry on what packages i offer and it is printed out and walked through at our first meeting. This brochure is as critical as my website - it needs to sing!

I'm looking for an eye-catching design that says:
Elegant
Modern
Clean
Crisp
Not cutesy or lovey-dovey thanks - we are more sophisticated and professional than that.

Update images to some of the latest weddings I've shot also. Let me know files and resolution you need. I've enabled right-click to download images on my site for a limited time. Please note that I retain copyright and will pursue any breeches.

Http://www.carlathornbey.com/Melbourne-wedding-photography
Updates

Thanks for all of your designs! Will take a few days to decide.

Target Market(s)

Australian Women aged 24-44

Industry/Entity Type

Wedding

Font styles to use
Other font styles liked:
• Century Gothic

Requirements
Must have
• Easy to print - does not have to be 6 A4 pages like the existing brochure
Nice to have
• Some full page images - The photos are supposed to be the hero here :-)
Should not have
• Not cutesy or lovey-dovey thanks - we are more sophisticated and professional than that.

No black backgrounds, I prefer a white thanks

No images in organic shaped boxes (like the rectangles in the logo - no thanks).
Keep the lines straight and sharp

```html
<!DOCTYPE html>
<html lang="en">
<head>
<meta charset="utf-8">
<title>Carla's Approach – Wedding Photography</title>
<link href="https://fonts.googleapis.com/css2?family=Questrial&display=swap" rel="stylesheet">
<style>
  :root {
    --salmon: #e8917a;
    --text: #666366;
    --heading-dark: #3f3c40;
    --hero-text: #5a5458;
    --paper: #ffffff;
  }
  * { margin: 0; padding: 0; box-sizing: border-box; }
  html, body { width: 848px; height: 1200px; overflow: hidden; background: var(--paper); }
  body { font-family: "Questrial", "Century Gothic", sans-serif; color: var(--text); position: relative; }

  .hero {
    position: absolute; left: 0; top: 0; width: 848px; height: 388px;
    background: linear-gradient(100deg, #6b5d6e 0%, #a59aa6 22%, #d9d3d8 42%, #f3eff1 62%, #f7f2f2 100%);
    overflow: hidden;
  }
  .hero-photo {
    position: absolute; inset: 0;
    background:
      radial-gradient(ellipse 260px 300px at 330px 330px, rgba(255,255,255,0.75), rgba(255,255,255,0) 70%),
      linear-gradient(90deg, rgba(60,50,65,0.55) 0%, rgba(60,50,65,0) 30%);
  }
  .hero-veil {
    position: absolute; inset: 0;
    background: linear-gradient(90deg, rgba(255,255,255,0) 0%, rgba(255,255,255,0.35) 45%, rgba(255,255,255,0.6) 100%);
  }
  .style-heading {
    position: absolute; right: 32px; top: 46px;
    font-size: 29px; line-height: 32px; font-weight: 400; color: var(--heading-dark); letter-spacing: 0.3px;
  }
  .style-copy {
    position: absolute; right: 32px; top: 80px; width: 540px;
    text-align: right; font-size: 17.4px; line-height: 24.4px; color: var(--hero-text);
    white-space: nowrap;
  }
  .approach-title {
    position: absolute; left: 0; right: 0; top: 292px; text-align: center;
    font-size: 54px; line-height: 54px; font-weight: 400; color: var(--salmon); letter-spacing: 0.5px;
    padding-left: 30px;
  }
  .approach-sub {
    position: absolute; left: 0; right: 0; top: 348px; text-align: center;
    font-size: 26px; line-height: 30px; color: var(--hero-text); padding-left: 26px;
  }
  .hero-rule {
    position: absolute; left: 0; top: 388px; width: 848px; height: 4px;
    background: linear-gradient(180deg, #8d8490, #d6d1d4);
  }

  .section-heading {
    position: absolute; font-size: 29px; font-weight: 400; color: var(--salmon); line-height: 32px;
  }
  .section-copy {
    position: absolute; font-size: 17.4px; line-height: 24.4px; color: var(--text); white-space: nowrap;
  }
  .formal-heading { left: 56px; top: 432px; }
  .formal-copy { left: 57px; top: 467px; width: 770px; }
  .presentation-heading { left: 55px; top: 652px; }
  .presentation-copy { left: 57px; top: 686px; width: 340px; }
  .season-heading { left: 56px; top: 962px; }
  .season-copy { left: 57px; top: 994px; width: 340px; }

  .photo { position: absolute; }
  .photo-couple-large {
    left: 406px; top: 656px; width: 410px; height: 274px;
    background: linear-gradient(135deg, #9a9a9a 0%, #6e6e6e 40%, #c9c9c9 75%, #8a8a8a 100%);
  }
  .photo-couple-small {
    left: 406px; top: 936px; width: 200px; height: 200px;
    background: linear-gradient(160deg, #8a8f7c 0%, #b7b3a2 45%, #3c3a40 100%);
  }
  .photo-bouquet {
    left: 613px; top: 936px; width: 203px; height: 200px;
    background: radial-gradient(circle at 50% 45%, #f4e6e3 0%, #e6cfcc 55%, #b9a7a3 100%);
  }
</style>
</head>
<body>
  <header class="hero">
    <div class="hero-photo" role="img" aria-label="Soft-toned photo of a bride and groom embracing, her hand on his back, lace wedding dress"></div>
    <div class="hero-veil"></div>
    <h2 class="style-heading">Style &amp; Approach</h2>
    <p class="style-copy">Carla can observe and capture your<br>wedding day in the background, quickly<br>and quietly taking photojournalistic pictures<br>rather than directing it if you prefer. Or she can<br>confidently play the role of Art Director and<br>instruct beautiful poses. Either way, what is most<br>important is that her clients are relaxed and<br>having a really great time on their wedding day!</p>
    <h1 class="approach-title">Carla's approach...</h1>
    <p class="approach-sub">Enjoy your special day!</p>
  </header>
  <div class="hero-rule"></div>

  <h2 class="section-heading formal-heading">Formal Photography</h2>
  <p class="section-copy formal-copy">Many of Carla's clients book her because of the easy-going approach she has.<br>They can get on with having a great time on their day without worrying about<br>formal photography. However, there are occasions when clients do want formal<br>family pictures, and Carla is more than happy to accommodate their requests.<br>In order to keep the disruption on the day to a minimum, we recommend that<br>Carla photographs no more than 6 groups, and a select number of the special<br>couple.</p>

  <h2 class="section-heading presentation-heading">Image Presentation</h2>
  <p class="section-copy presentation-copy">The most professional way of<br>presenting clients with their<br>photographs is in an elegantly<br>designed photo book. Carla's clients<br>only pay one fixed price for the<br>photography, regardless of how<br>many images taken. There are no<br>hard sell procedures to go through,<br>and the completed book is<br>prepared within 2-6 weeks after the<br>wedding day.</p>

  <h2 class="section-heading season-heading">Time of Year</h2>
  <p class="section-copy season-copy">Signature pictures can be taken on<br>overcast days or winter months.<br>Don't worry if the sky is not perfectly<br>blue. In the end, regardless of the<br>weather – it's the timeless mood of<br>the day that Carla strives to capture.</p>

  <div class="photo photo-couple-large" role="img" aria-label="Black and white portrait of the bride and groom smiling together outdoors"></div>
  <div class="photo photo-couple-small" role="img" aria-label="Muted colour portrait of the bride and groom standing among willow trees"></div>
  <div class="photo photo-bouquet" role="img" aria-label="Close-up of a bouquet of pale pink and cream roses"></div>
</body>
</html>
```